Tarjetas de visita para empresa de aluminio

Empresa con mas de 40 años vendiendo perfiles de aluminio.
Somos fábrica y almacén, queremos renovar la tarjeta de presentación de nuestros comerciales dando una imgen innovadora y tecnógica mezclado con la calidez del respeto al medio ambiente.
Añado el logo de la empresa y actual cara trasera de la tarjeta de visita, el logo es el simbolo WM y la marca TRAVENIC EXTRUSION, la frase 2extrusion y lacado de aluminio" debe cambiarse por "Diseño, extrusión, lacado, anodizado y mecanizado de precisión de aluminio" o en su defecto incluir todos esos servicios que hacemos o una frase mas pegadiza.

We are an aluminium factory, we produce and stock profiles of aluminium.
we want to renew visit card of our sellers, we are looking for something that show innovation, tecnology and environment respect.
Upload our actual logo and back of visit card, logo WM and brand TRAVENIC EXTRUSION must be keept.
Text "Extrusion y lacado de aluminio" must be changed for "Diseño, extrusion, lacado, anodizado y mecanizado de precisión de aluminio" or something like that

```html
<!DOCTYPE html>
<html lang="es">
<head>
<meta charset="utf-8">
<title>Tarjetas de visita · Travenic Extrusion</title>
<link href="https://fonts.googleapis.com/css2?family=Poppins:wght@400;600;700&display=swap" rel="stylesheet">
<style>
  :root {
    --backdrop: #e3e4e8;
    --card-deep: #053456;
    --card-light: #0b628b;
    --text-main: #b9c9d6;
    --text-soft: #a6b9c8;
    --mark-faint: rgba(120, 175, 210, 0.13);
  }
  * { margin: 0; padding: 0; box-sizing: border-box; }
  html, body {
    width: 1200px; height: 1200px; overflow: hidden;
    background: var(--backdrop);
    font-family: "Poppins", sans-serif;
  }
  .sheet { position: relative; width: 1200px; height: 1200px; }
  .card {
    position: absolute; left: 286px; width: 629px; height: 359px;
    background: linear-gradient(35deg, var(--card-deep) 0%, #07476d 45%, var(--card-light) 100%);
    overflow: hidden;
  }
  .card--front { top: 195px; }
  .card--back { top: 645px; }

  .faint-mark {
    position: absolute; left: 230px; top: 30px;
    font-weight: 700; font-size: 300px; line-height: 1;
    color: var(--mark-faint); letter-spacing: -10px;
  }

  .brand-mark {
    position: absolute; display: flex; align-items: center; gap: 10px;
    color: var(--text-main); font-weight: 700;
  }
  .card--front .brand-mark { left: 40px; top: 46px; font-size: 50px; line-height: 1; }
  .brand-dot { width: 16px; height: 16px; border-radius: 50%; background: var(--text-main); }

  .brand-block { position: absolute; color: var(--text-main); }
  .card--front .brand-block { left: 182px; top: 46px; text-align: center; }
  .brand-name { font-weight: 700; font-size: 21px; line-height: 1.1; letter-spacing: 0.2px; }
  .brand-tagline { font-weight: 600; font-size: 11.2px; line-height: 1.25; margin-top: 4px; }

  .person { position: absolute; left: 0; right: 0; top: 152px; text-align: center; }
  .person-name { font-weight: 700; font-size: 25px; color: var(--text-main); line-height: 1.2; }
  .person-role { font-weight: 400; font-size: 17px; letter-spacing: 6px; color: var(--text-soft); margin-top: 2px; }

  .contact { position: absolute; color: var(--text-main); font-weight: 600; font-size: 14.5px; line-height: 19px; }
  .contact--left { left: 36px; top: 248px; }
  .contact--right { right: 36px; top: 248px; text-align: right; }
  .contact-row { display: flex; align-items: center; gap: 8px; height: 19px; }
  .contact--right .contact-row { justify-content: flex-end; }
  .contact-row--indent { padding-left: 25px; }
  .icon { width: 17px; height: 17px; flex: none; }
  .icon * { fill: none; stroke: var(--text-main); stroke-width: 1.6; stroke-linecap: round; stroke-linejoin: round; }
  .icon .solid { fill: var(--text-main); stroke: none; }

  .card--back .brand-mark {
    left: 0; right: 0; top: 98px; justify-content: center;
    font-size: 96px; line-height: 1; gap: 18px;
  }
  .card--back .brand-dot { width: 26px; height: 26px; }
  .card--back .brand-block { left: 0; right: 0; top: 234px; text-align: center; }
  .card--back .brand-name { font-size: 22px; }
</style>
</head>
<body>
<main class="sheet">

  <section class="card card--front">
    <div class="faint-mark" aria-hidden="true">WM</div>

    <div class="brand-mark"><span>WM</span><span class="brand-dot"></span></div>
    <div class="brand-block">
      <div class="brand-name">TRAVENIC EXTRUSION</div>
      <div class="brand-tagline">Diseño, extrusión, lacado, anodizado y<br>mecanizado de precisión de aluminio</div>
    </div>

    <div class="person">
      <div class="person-name">Daniel Ortega Ruiz</div>
      <div class="person-role">COMERCIAL</div>
    </div>

    <div class="contact contact--left">
      <div class="contact-row">
        <svg class="icon" viewBox="0 0 20 20"><path class="solid" d="M10 1.5a6 6 0 0 0-6 6c0 4.5 6 11 6 11s6-6.5 6-11a6 6 0 0 0-6-6zm0 8.3a2.3 2.3 0 1 1 0-4.6 2.3 2.3 0 0 1 0 4.6z"/></svg>
        <span>Pol. Ind. Los Olivares C/ 3 N 12</span>
      </div>
      <div class="contact-row contact-row--indent">41990 VILLANUEVA DEL RÍO (Sevilla)</div>
      <div class="contact-row contact-row--indent">Apartado de Correos 245</div>
      <div class="contact-row">
        <svg class="icon" viewBox="0 0 20 20"><rect x="1.5" y="4" width="17" height="12"/><path d="M1.5 4l8.5 7 8.5-7M1.5 16l6-6M18.5 16l-6-6"/></svg>
        <span>danielortega@travenic.com</span>
      </div>
    </div>

    <div class="contact contact--right">
      <div class="contact-row">
        <span>600 12 34 56</span>
        <svg class="icon" viewBox="0 0 20 20"><rect x="6" y="1.5" width="8" height="17" rx="1.5" transform="rotate(-20 10 10)"/></svg>
      </div>
      <div class="contact-row">
        <span>955 00 11 22</span>
        <svg class="icon" viewBox="0 0 20 20"><path d="M4 2h3.5l1.5 4-2 1.5a10 10 0 0 0 5.5 5.5l1.5-2 4 1.5V16a2 2 0 0 1-2 2A15 15 0 0 1 2 4a2 2 0 0 1 2-2z"/></svg>
      </div>
      <div class="contact-row">
        <span>955 00 11 33</span>
        <svg class="icon" viewBox="0 0 20 20"><rect x="5" y="2" width="10" height="5"/><rect x="2" y="7" width="16" height="7" rx="1"/><rect x="5" y="12" width="10" height="6"/></svg>
      </div>
      <div class="contact-row">
        <span>www.travenic.com</span>
        <svg class="icon" viewBox="0 0 20 20"><circle cx="10" cy="10" r="8.2"/><ellipse cx="10" cy="10" rx="3.6" ry="8.2"/><path d="M1.8 10h16.4M3 6h14M3 14h14"/></svg>
      </div>
    </div>
  </section>

  <section class="card card--back">
    <div class="brand-mark"><span>WM</span><span class="brand-dot"></span></div>
    <div class="brand-block">
      <div class="brand-name">TRAVENIC EXTRUSION</div>
      <div class="brand-tagline">Diseño, extrusión, lacado, anodizado y<br>mecanizado de precisión de aluminio</div>
    </div>
  </section>

</main>
</body>
</html>
```